Birchline Septic Solutions

Would like to see some single sided ones but would also like to see some double sided with one sided only being the logo. Owners name is Tom Halvick. Phone number is 555-214-0387
Services are pumping, inspections, installs, and repairs

Contact Information for Business Card

555-241-0387 Tom Halvick Fernbrook, OH

```html
<!DOCTYPE html>
<html lang="en">
<head>
<meta charset="utf-8">
<title>Birchline Septic Solutions – Business Card</title>
<link href="https://fonts.googleapis.com/css2?family=Poppins:wght@400;600;800&display=swap" rel="stylesheet">
<style>
  :root {
    --ink: #0b0b0b;
    --paper: #ffffff;
    --teal: #2bbcb3;
    --backdrop: #d9dcdf;
    --muted: #9aa0a6;
  }
  * { box-sizing: border-box; margin: 0; padding: 0; }
  html, body { width: 1200px; height: 900px; overflow: hidden; }
  body {
    background: var(--backdrop);
    font-family: "Poppins", sans-serif;
    display: flex;
    flex-direction: column;
    align-items: center;
    justify-content: center;
    gap: 60px;
  }
  .card {
    position: relative;
    width: 630px;
    height: 360px;
    overflow: hidden;
    box-shadow: 0 10px 30px rgba(0,0,0,.18);
  }
  .card--front { background: var(--paper); }
  .card--back { background: var(--ink); display: flex; align-items: center; justify-content: center; }
  .card__shapes { position: absolute; inset: 0; }

  .brand {
    position: absolute;
    display: flex;
    align-items: center;
    gap: 12px;
    font-weight: 800;
    text-transform: uppercase;
    letter-spacing: 1px;
  }
  .brand__mark { width: 16px; height: 16px; background: var(--teal); }
  .card--front .brand { left: 150px; top: 48px; color: var(--ink); font-size: 25px; }
  .card--back .brand { position: static; color: var(--paper); font-size: 30px; }

  .contact {
    position: absolute;
    left: 40px;
    top: 230px;
    color: var(--paper);
    font-size: 17px;
    font-weight: 600;
    line-height: 1.6;
    list-style: none;
  }
  .contact__item { display: flex; align-items: center; gap: 8px; }
  .contact__icon { width: 16px; height: 16px; }

  .owner {
    position: absolute;
    right: 28px;
    top: 152px;
    color: var(--paper);
    font-size: 27px;
    font-weight: 800;
    text-transform: uppercase;
  }

  .services {
    position: absolute;
    right: 28px;
    top: 238px;
    list-style: none;
    color: var(--paper);
    font-size: 17px;
    font-weight: 600;
    text-transform: uppercase;
    text-align: right;
    line-height: 36px;
  }
</style>
</head>
<body>

  <section class="card card--front" aria-label="Business card front">
    <svg class="card__shapes" width="630" height="360" viewBox="0 0 630 360" aria-hidden="true">
      <!-- teal accent edge -->
      <polygon points="0,195 40,195 0,300" fill="var(--teal)"/>
      <!-- contact panel -->
      <polygon points="30,195 300,195 250,360 0,360 0,290" fill="var(--ink)"/>
      <!-- name tag -->
      <polygon points="385,140 630,140 630,200 365,200" fill="var(--ink)"/>
      <!-- services band -->
      <polygon points="320,215 630,215 630,350 280,350" fill="var(--teal)"/>
      <line x1="308" y1="262" x2="630" y2="262" stroke="var(--paper)" stroke-width="2"/>
      <line x1="296" y1="300" x2="630" y2="300" stroke="var(--paper)" stroke-width="2"/>
    </svg>

    <div class="brand"><span class="brand__mark"></span>Birchline Septic Solutions</div>

    <ul class="contact">
      <li class="contact__item">
        <svg class="contact__icon" viewBox="0 0 16 16" aria-hidden="true"><circle cx="8" cy="8" r="7" fill="none" stroke="var(--teal)" stroke-width="1.5"/><path d="M5.5 4.5c.4 3 2.6 5.5 5.5 6.5l.8-1.3-1.6-.9-.7.7c-1-.6-1.9-1.5-2.4-2.6l.7-.6-.8-1.7z" fill="var(--paper)"/></svg>
        555-241-0387
      </li>
      <li class="contact__item">
        <svg class="contact__icon" viewBox="0 0 16 16" aria-hidden="true"><circle cx="8" cy="8" r="7" fill="none" stroke="var(--teal)" stroke-width="1.5"/><path d="M8 3.5a3 3 0 0 0-3 3c0 2.2 3 5.5 3 5.5s3-3.3 3-5.5a3 3 0 0 0-3-3z" fill="var(--paper)"/><circle cx="8" cy="6.5" r="1" fill="var(--ink)"/></svg>
        Fernbrook, OH
      </li>
    </ul>

    <h1 class="owner">Tom Halvick</h1>

    <ul class="services">
      <li>Pumping</li>
      <li>Inspections</li>
      <li>Installs, and Repairs</li>
    </ul>
  </section>

  <section class="card card--back" aria-label="Business card back">
    <div class="brand"><span class="brand__mark"></span>Birchline Septic Solutions</div>
  </section>

</body>
</html>
```